Original business card of a small accounting firm

My firm specializes in accounting and taxes for small businesses. I'm looking for an original and creative business card as a marketing tool to give to prospective clients; however since we are a professional firm the card must also appear professional. I'm uploading a few examples of what I believe may fit my needs. Please feel free to use them as a jumping off point. Lastly, I'm uploading the company logo which I'd like to be the focal point on the back of the card and somewhat incorporated on the front on a smaller scale. I hope my description was helpful.
Target Market(s)
Tax clients and small businesses
Industry/Entity Type
Accounting
Contact Information for Business Card
Gerald Whitcombe
Certified Public Accountant │President
Whitcombe Advisors
T│ (555) 417-2863
Email│GWhitcombe@WhitcombeAdvisors.example
Look and feel
Each slider illustrates characteristics of the customer's brand and the style your logo design should communicate.

```html
<!DOCTYPE html>
<html lang="en">
<head>
<meta charset="utf-8">
<title>Whitcombe Advisors – Business Card</title>
<link href="https://fonts.googleapis.com/css2?family=Open+Sans:wght@400;600;700&display=swap" rel="stylesheet">
<style>
  :root {
    --backdrop: #e4e4e6;
    --card-black: #0b0b0d;
    --card-black-soft: #25262b;
    --card-white: #ffffff;
    --ink: #2b2b2e;
    --ink-soft: #55565b;
    --brand-blue: #2f5fb8;
    --brand-blue-deep: #1d2f86;
    --brand-blue-light: #4a8fe0;
    --silver: #c9cacd;
    --faint: #ededee;
  }
  * { box-sizing: border-box; margin: 0; padding: 0; }
  html, body { width: 1200px; height: 852px; overflow: hidden; }
  body {
    background: var(--backdrop);
    font-family: "Open Sans", Arial, sans-serif;
    position: relative;
  }
  .card {
    position: absolute;
    top: 283px;
    width: 500px;
    height: 286px;
    border-radius: 18px;
    overflow: hidden;
    box-shadow: 0 6px 18px rgba(0,0,0,.18);
  }

  /* Back of card */
  .card-back {
    left: 70px;
    background: radial-gradient(ellipse at 50% 45%, var(--card-black-soft) 0%, var(--card-black) 70%);
    display: flex;
    flex-direction: column;
    align-items: center;
    justify-content: center;
    gap: 10px;
  }
  .back-lockup { display: flex; align-items: center; gap: 14px; }
  .brand-square {
    width: 26px; height: 26px;
    background: var(--brand-blue);
  }
  .back-name {
    font-size: 34px;
    font-weight: 600;
    color: var(--silver);
    letter-spacing: .5px;
  }
  .back-tagline {
    font-size: 10.5px;
    letter-spacing: 3px;
    color: var(--silver);
    text-transform: uppercase;
  }

  /* Front of card */
  .card-front {
    left: 630px;
    background: var(--card-white);
  }
  .accent-strip {
    position: absolute;
    left: 0; top: 0; bottom: 0;
    width: 30px;
    background: linear-gradient(90deg, var(--brand-blue-deep), var(--brand-blue-light) 55%, var(--brand-blue-deep));
    border-right: 3px solid #3b3c42;
  }
  .front-brand {
    position: absolute;
    top: 30px; right: 26px;
    text-align: right;
  }
  .front-name {
    font-size: 22px;
    font-weight: 600;
    color: var(--ink);
  }
  .front-tagline {
    font-size: 7.5px;
    letter-spacing: 1.8px;
    color: var(--ink-soft);
    text-transform: uppercase;
  }
  .watermark-name {
    position: absolute;
    right: 34px;
    top: 100px;
    writing-mode: vertical-rl;
    font-size: 22px;
    letter-spacing: 3px;
    color: var(--faint);
    font-weight: 400;
    text-transform: uppercase;
    line-height: 1.2;
  }
  .person {
    position: absolute;
    left: 58px; top: 110px;
  }
  .person-name {
    font-size: 17px;
    font-weight: 700;
    color: var(--brand-blue-deep);
  }
  .person-title {
    font-size: 10.5px;
    color: var(--ink);
    line-height: 1.35;
    margin-top: 2px;
  }
  .contact-list {
    position: absolute;
    left: 58px; top: 190px;
    list-style: none;
  }
  .contact-item {
    display: flex;
    align-items: center;
    gap: 10px;
    font-size: 11.5px;
    color: var(--ink);
    margin-bottom: 6px;
  }
  .contact-icon { width: 12px; height: 12px; flex: none; }
</style>
</head>
<body>

  <section class="card card-back">
    <div class="back-lockup">
      <span class="brand-square"></span>
      <span class="back-name">Whitcombe Advisors</span>
    </div>
    <p class="back-tagline">Small Business Accounting and Taxes</p>
  </section>

  <section class="card card-front">
    <div class="accent-strip"></div>

    <div class="front-brand">
      <p class="front-name">Whitcombe Advisors</p>
      <p class="front-tagline">Small Business Accounting and Taxes</p>
    </div>

    <p class="watermark-name">Gerald<br>Whitcombe</p>

    <div class="person">
      <p class="person-name">Gerald Whitcombe</p>
      <p class="person-title">Certified Public Accountant/<br>President Whitcombe Advisors</p>
    </div>

    <ul class="contact-list">
      <li class="contact-item">
        <svg class="contact-icon" viewBox="0 0 12 12" aria-hidden="true">
          <path d="M1 4 Q6 0 11 4 L9 5.5 L8 4 Q6 3.4 4 4 L3 5.5 Z" fill="#2f5fb8"/>
          <rect x="2.5" y="6" width="7" height="5" rx="1" fill="#2f5fb8"/>
        </svg>
        (555) 417-2863
      </li>
      <li class="contact-item">
        <svg class="contact-icon" viewBox="0 0 12 12" aria-hidden="true">
          <rect x="0.5" y="2" width="11" height="8" rx="1" fill="#2f5fb8"/>
          <path d="M1 2.5 L6 6.5 L11 2.5" stroke="#fff" stroke-width="1" fill="none"/>
        </svg>
        GWhitcombe@WhitcombeAdvisors.example
      </li>
      <li class="contact-item">
        <svg class="contact-icon" viewBox="0 0 12 12" aria-hidden="true">
          <circle cx="6" cy="6" r="5.3" fill="#2f5fb8"/>
          <path d="M0.8 6 H11.2 M6 0.8 Q2.8 6 6 11.2 M6 0.8 Q9.2 6 6 11.2" stroke="#fff" stroke-width=".8" fill="none"/>
        </svg>
        www.WhitcombeAdvisors.example
      </li>
    </ul>
  </section>

</body>
</html>
```